International Fundraising Consultancy needs a new PowerPoint Design

We train international nonprofits on how to fundraise globally. We plan to keep our current logo design and color, as we love the color orange, but want a cleaner, fresher, less cluttered template for our PowerPoint presentations. The finished product needs to be easy to edit, and include template slides that can feature tables, graphics and images. We would like a color scheme for graphics.The layout should be lighter, clear, attractive and easy to read and understand. We also want to use the same template for webinar slides. We have attached an example of our current PowerPoint template with identifying client information removed. The green slide that looks like a clapperboard fro a film is basically just a placeholder that indicates a break for an interactive exercise.

Target Market(s)

Board members, staff members, museum executives, leadership of NGOs, top businesspeople in Europe, many with a modern sense of aesthetics in the art world

Industry/Entity Type

Cleaner

Font styles to use
Sans Serif

Colors
f78f20
f37022

Requirements
Must have
• Orange colors, keep our Vormelinck logo
• Good templates for tables, photos and graphics

```html
<!DOCTYPE html>
<html lang="en">
<head>
<meta charset="utf-8">
<title>Vormelinck &amp; Associates – Title Slide</title>
<link href="https://fonts.googleapis.com/css2?family=Exo+2:wght@300&family=Roboto+Condensed:wght@400&family=Arimo:wght@700&display=swap" rel="stylesheet">
<style>
  :root {
    --orange: #f37022;
    --orange-light: #f78f20;
    --charcoal: #444444;
    --white: #ffffff;
    --photo-warm: #c77a4e;
    --photo-pale: #d9cfc2;
  }
  html, body {
    margin: 0;
    padding: 0;
    overflow: hidden;
    background: var(--white);
  }
  .slide {
    position: relative;
    width: 1200px;
    height: 849px;
    overflow: hidden;
    background: var(--white);
  }
  .slide-shapes {
    position: absolute;
    inset: 0;
  }
  .brand {
    position: absolute;
    left: 82px;
    top: 92px;
    display: flex;
    align-items: center;
    gap: 22px;
  }
  .brand-dot {
    width: 36px;
    height: 36px;
    border-radius: 50%;
    background: var(--orange-light);
  }
  .brand-text {
    display: flex;
    flex-direction: column;
  }
  .brand-name {
    font-family: "Roboto Condensed", sans-serif;
    font-weight: 400;
    font-size: 37px;
    line-height: 1;
    color: var(--orange);
  }
  .brand-tagline {
    font-family: "Roboto Condensed", sans-serif;
    font-size: 18px;
    line-height: 1.2;
    margin-top: 4px;
    color: var(--orange);
  }
  .headline {
    position: absolute;
    left: 94px;
    top: 276px;
    margin: 0;
    font-family: "Exo 2", sans-serif;
    font-weight: 300;
    font-size: 52px;
    line-height: 57px;
    color: var(--white);
  }
  .website {
    position: absolute;
    left: 777px;
    top: 786px;
    font-family: "Arimo", sans-serif;
    font-weight: 700;
    font-size: 18px;
    color: var(--orange-light);
  }
</style>
</head>
<body>
  <main class="slide">
    <svg class="slide-shapes" width="1200" height="849" viewBox="0 0 1200 849">
      <defs>
        <linearGradient id="photo-tone" x1="0" y1="0" x2="1" y2="1">
          <stop offset="0" stop-color="var(--photo-pale)"/>
          <stop offset="0.5" stop-color="var(--photo-warm)"/>
          <stop offset="1" stop-color="#b9a58f"/>
        </linearGradient>
      </defs>
      <path class="title-band" fill="var(--charcoal)"
            d="M0,230 L466,230 C830,236 1080,560 1103,849 L0,849 Z"/>
      <path class="feature-photo" role="img"
            aria-label="Photo of a small child drinking from a cup in front of terracotta water filter jars"
            fill="url(#photo-tone)" stroke="var(--white)" stroke-width="8"
            d="M-10,556 L300,556 C520,562 640,700 664,860 L-10,860 Z"/>
    </svg>

    <header class="brand">
      <span class="brand-dot"></span>
      <div class="brand-text">
        <span class="brand-name">Vormelinck &amp; Associates</span>
        <span class="brand-tagline">Fundraising Counsel</span>
      </div>
    </header>

    <h1 class="headline">You helped launch<br>our international<br>program quickly and<br>efficiently...</h1>

    <span class="website">www.vormelinck.com</span>
  </main>
</body>
</html>
```